out of the box Business Card Design for a Manufacturer / Distributor

We are a manufarturer and distributor of products.
the company name is VORTANI (Pic attached)

the picture is NOT a must have on the business Card.

the Business Card should look really professional and/or special, so out of the box thinking is welcome.

there should be 2 Adresses on the Business Card for Main and Branch Office.
Email Adress, homepage, Name is required
NO Phone Number

Our working field:
Private Labeling
high Quality Production
direct distribution
warehousing
trademark registration
legal support

Main Office:
Kornblumenweg 14
08352 Erlenfeld
Germany

Branch Office:
Daska Lane
Kelmabad
Pakistan

Names:
Lukas Feldhaus (Owner)
Imran Qureshi (Owner)

Email:
lukas@vortani-example.com
imran@vortani-example.com

homepage:
vortani-example.com

Industry/Entity Type

Manufacturer Distributer

Contact Information for Business Card

Vortani

Requirements
Must have
• Names, both office Adresses, email, homepage
Should not have
• Phone Number

```html
<!DOCTYPE html>
<html lang="en">
<head>
<meta charset="utf-8">
<title>VORTANI Business Card</title>
<link rel="stylesheet" href="https://fonts.googleapis.com/css2?family=Lato:wght@400;700&family=Work+Sans:wght@400;500;600&display=swap">
<style>
  :root {
    --backdrop: #9c9d9f;
    --front-card: #555555;
    --plate-top: #4b4b4b;
    --plate-bottom: #646464;
    --back-frame: #f1f1f0;
    --back-panel: #e3e2e0;
    --accent-bar: #cbcbca;
    --ink: #1b1b1b;
    --ink-soft: #4a4a4a;
    --rule: #9a9a9a;
    --white: #ffffff;
  }
  * { margin: 0; padding: 0; box-sizing: border-box; }
  html, body { width: 1200px; height: 1000px; overflow: hidden; }
  body {
    background: var(--backdrop);
    position: relative;
    font-family: "Work Sans", Arial, sans-serif;
    color: var(--ink);
  }

  /* Front face */
  .card-front {
    position: absolute; left: 313px; top: 145px;
    width: 575px; height: 323px;
    background: var(--front-card);
  }
  .brand-plate {
    position: absolute; left: 114px; top: 85px;
    width: 343px; height: 143px;
    background: linear-gradient(135deg, var(--plate-top), var(--plate-bottom));
    box-shadow: 3px 4px 6px rgba(0,0,0,0.35);
    display: flex; align-items: center; justify-content: center; gap: 14px;
  }
  .brand-dot {
    flex: none;
    width: 44px; height: 44px; border-radius: 50%;
    background: var(--white);
  }
  .brand-name {
    font-family: "Lato", Arial, sans-serif;
    font-weight: 400;
    font-size: 44px;
    letter-spacing: 1px;
    line-height: 1;
    color: var(--white);
  }
  .front-url {
    position: absolute; left: 0; right: 0; top: 248px;
    text-align: center;
    font-size: 15px; color: var(--white);
    padding-left: 10px;
  }
  .front-url b { font-weight: 600; }

  /* Back face */
  .card-back {
    position: absolute; left: 313px; top: 531px;
    width: 575px; height: 325px;
    background: var(--back-frame);
  }
  .back-panel {
    position: absolute; left: 19px; top: 16px;
    width: 540px; height: 295px;
    background: var(--back-panel);
  }
  .accent-bar {
    position: absolute; left: 0; top: 59px;
    width: 35px; height: 14px;
    background: var(--accent-bar);
  }
  .person { position: absolute; left: 49px; top: 54px; }
  .person-name { font-size: 18px; font-weight: 500; line-height: 22px; }
  .person-role { font-size: 14px; color: var(--ink-soft); }

  .services { position: absolute; left: 357px; top: 37px; font-size: 12.5px; line-height: 16.5px; }
  .services-title { font-weight: 600; padding-left: 15px; font-size: 13px; }
  .services ul { list-style: none; }
  .services li { display: flex; align-items: center; gap: 7px; }
  .services li::before {
    content: ""; width: 8px; height: 8px; border-radius: 50%;
    background: var(--rule);
  }

  .email {
    position: absolute; left: 47px; top: 173px;
    width: 216px; padding-bottom: 4px;
    border-bottom: 1.5px solid var(--rule);
    font-size: 13px;
  }
  .email b { font-weight: 600; }
  .offices { position: absolute; left: 48px; top: 201px; display: flex; font-size: 11.5px; line-height: 16px; }
  .office { color: var(--ink-soft); white-space: nowrap; }
  .office-main { width: 112px; }
  .office strong { display: block; font-size: 13px; font-weight: 600; color: var(--ink); }
  .office .country { font-size: 13px; font-weight: 600; color: var(--ink); }

  .back-brand { position: absolute; left: 300px; top: 166px; }
  .back-brand .logo-row { display: flex; align-items: center; gap: 12px; }
  .back-brand .brand-dot { width: 42px; height: 42px; background: var(--ink); }
  .back-brand .brand-name { font-size: 34px; color: var(--ink); letter-spacing: 0.5px; }
  .back-url { font-size: 14.5px; margin-left: 54px; margin-top: 2px; }
  .back-url b { font-weight: 600; }
</style>
</head>
<body>
  <section class="card-front">
    <div class="brand-plate">
      <span class="brand-dot"></span>
      <span class="brand-name">VORTANI</span>
    </div>
    <p class="front-url">www.<b>vortani-example</b>.com</p>
  </section>

  <section class="card-back">
    <div class="back-panel"></div>
    <span class="accent-bar"></span>

    <div class="person">
      <p class="person-name">Lukas Feldhaus</p>
      <p class="person-role">Owner</p>
    </div>

    <div class="services">
      <p class="services-title">Our working field:</p>
      <ul>
        <li>Private Labeling</li>
        <li>High Quality Production</li>
        <li>Direct distribution</li>
        <li>Warehousing</li>
        <li>Trademark Registration</li>
        <li>Legal Support</li>
      </ul>
    </div>

    <p class="email">lukas@<b>vortani-example</b>.com</p>

    <div class="offices">
      <div class="office office-main">
        <strong>Main Office:</strong>
        Kornblumenweg 14<br>08352 Erlenfeld<br>
        <span class="country">Germany</span>
      </div>
      <div class="office office-branch">
        <strong>Branch Office:</strong>
        Daska Lane<br>Kelmabad<br>
        <span class="country">Pakistan</span>
      </div>
    </div>

    <div class="back-brand">
      <div class="logo-row">
        <span class="brand-dot"></span>
        <span class="brand-name">VORTANI</span>
      </div>
      <p class="back-url">www.<b>vortani-example</b>.com</p>
    </div>
  </section>
</body>
</html>
```